Security Consulting Firm needs brochure to be used for advertisement and sales

Need a brochure design for a new security consulting firm based in Metro Detroit called "K. Halvern Security Consulting, LLC" We provide consulting services related to safety and security for our clients. I have attached a file that contains excerpts from our business summary for info to be used (does not have to be word for work or exact), business contact info as well as statistics that i would like added somewhere. I also attached the company logo for use. I would like the logos for Pagemoot, CareerWeft and Snapvane somewhere on the brochure as well. Lastly , I would like the final design to communicate strength, safety, investigation and protection. Thank you
Target Market(s)
Corporate, schools, places of worship, large events, VIP
Industry/Entity Type
Business Consultant
Colors

```html
<!DOCTYPE html>
<html lang="en">
<head>
<meta charset="utf-8">
<title>K. Halvern Security Consulting, LLC — Brochure</title>
<link rel="stylesheet" href="https://fonts.googleapis.com/css2?family=Barlow:wght@300;400;500;700;800&family=Barlow+Condensed:wght@500;600;700&display=swap">
<style>
  :root{
    --navy:#2a2d86;
    --royal:#2f2f9a;
    --sky:#2b7bc2;
    --bar:#2a7ec4;
    --ink:#0b0b0e;
    --white:#ffffff;
    --red:#d2232a;
    --photo-dark:#121317;
    --photo-mid:#3d4048;
  }
  *{margin:0;padding:0;box-sizing:border-box}
  html,body{width:851px;height:1200px;overflow:hidden;background:#fff}
  .brochure{position:relative;width:851px;height:1200px;overflow:hidden;background:var(--white);font-family:"Barlow",sans-serif;color:var(--white)}
  .backdrop{position:absolute;inset:0}
  .title{position:absolute;left:58px;top:42px;line-height:.9}
  .title .line1{font-weight:800;font-size:62px;color:var(--sky);letter-spacing:-1px;display:block}
  .title .line2{font-weight:800;font-size:70px;color:var(--navy);letter-spacing:-1px;display:block}
  .title .line3{font-weight:400;font-size:52px;color:var(--navy);display:block;margin-top:4px}
  .brand{position:absolute;left:545px;top:92px;width:298px;height:84px;background:var(--white);display:flex;align-items:center;gap:10px;padding:0 12px}
  .brand-mark{width:22px;height:22px;background:var(--navy);flex:none}
  .brand-name{font-family:"Barlow Condensed",sans-serif;font-weight:700;font-size:21px;color:var(--ink);line-height:1.05;letter-spacing:.5px}
  .photo-guard{position:absolute;left:290px;top:259px;width:561px;height:517px}
  .about{position:absolute;left:62px;top:283px;width:460px}
  h2{font-family:"Barlow Condensed",sans-serif;font-weight:700;font-size:33px;color:var(--sky);line-height:1}
  .about p{font-size:15.5px;font-weight:500;line-height:1.2;margin-top:6px}
  .services{position:absolute;left:62px;top:469px}
  .services ul{list-style:none;margin-top:8px}
  .services li{font-family:"Barlow Condensed",sans-serif;font-weight:600;font-size:20.5px;line-height:23.5px;padding-left:28px;position:relative}
  .services li::before{content:"";position:absolute;left:6px;top:7px;border-left:9px solid #bfc3cc;border-top:5px solid transparent;border-bottom:5px solid transparent}
  .hex{position:absolute}
  .facts{position:absolute;left:397px;top:793px;width:430px}
  .facts h2{font-size:31px;color:#8fb6ea}
  .facts ul{list-style:none;margin-top:6px}
  .facts li{font-size:13.6px;line-height:14.5px;padding-left:22px;position:relative;margin-bottom:14px}
  .facts li::before{content:"";position:absolute;left:0;top:12px;border-left:9px solid var(--red);border-top:5px solid transparent;border-bottom:5px solid transparent}
  .contact-bar{position:absolute;left:0;top:1070px;width:851px;height:80px;background:var(--bar);display:flex;align-items:center;padding-left:46px}
  .call{display:flex;align-items:center;gap:14px;font-family:"Barlow Condensed",sans-serif;font-size:40px;font-weight:500;white-space:nowrap}
  .call strong{font-family:"Barlow",sans-serif;font-weight:700;font-size:38px}
  .call-icon{width:30px;height:30px;background:var(--navy);display:flex;align-items:center;justify-content:center}
  .web{margin-left:38px;font-family:"Barlow Condensed",sans-serif;font-weight:600;font-size:19px;line-height:21px}
  .social{position:absolute;left:210px;top:1158px;display:flex;gap:36px}
  .social span{display:flex;align-items:center;gap:8px;font-family:"Barlow Condensed",sans-serif;font-weight:600;font-size:15px;color:var(--white)}
  .social i{width:14px;height:14px;background:var(--sky);display:block}
</style>
</head>
<body>
<main class="brochure">
  <svg class="backdrop" width="851" height="1200" viewBox="0 0 851 1200" aria-hidden="true">
    <defs>
      <linearGradient id="blueBand" x1="0" y1="0" x2="1" y2="1">
        <stop offset="0" stop-color="#3a3aa8"/>
        <stop offset="1" stop-color="#24247a"/>
      </linearGradient>
    </defs>
    <polygon points="552,0 851,0 851,259 457,259" fill="url(#blueBand)"/>
    <rect x="0" y="259" width="851" height="517" fill="var(--ink)"/>
    <polygon points="260,776 851,776 851,1200 0,1200 0,1150 95,1150" fill="url(#blueBand)"/>
    <polygon points="0,1150 95,1150 0,1200" fill="#fff"/>
    <polygon points="0,1150 110,1150 95,1200 0,1200" fill="#fff"/>
  </svg>

  <h1 class="title">
    <span class="line1">KHALVERN</span>
    <span class="line2">SECURITY</span>
    <span class="line3">CONSULTING</span>
  </h1>

  <div class="brand">
    <span class="brand-mark"></span>
    <span class="brand-name">K. HALVERN<br>SECURITY CONSULTING, LLC</span>
  </div>

  <svg class="photo-guard" viewBox="0 0 561 517" role="img" aria-label="Photo of a security officer in a black cap and jacket with SECURITY lettering, speaking into an earpiece">
    <defs>
      <linearGradient id="guardTone" x1="0" y1="0" x2="1" y2="0.6">
        <stop offset="0" stop-color="#0b0b0e"/>
        <stop offset=".45" stop-color="var(--photo-dark)"/>
        <stop offset=".8" stop-color="var(--photo-mid)"/>
        <stop offset="1" stop-color="#23252b"/>
      </linearGradient>
    </defs>
    <rect width="561" height="517" fill="url(#guardTone)"/>
  </svg>

  <section class="about">
    <h2>ABOUT US</h2>
    <p>K. Halvern Security Consulting, LLC is a Metro Detroit based full-service consulting agency committed to the ever necessary safety of our clients and their assets, while always providing CPR; Commitment, Protection and Results. K. Halvern Security Consulting, LLC is owned and operated by an active duty law enforcement officer, who has a vast array of experience and training in high-risk/high-threat level operations.</p>
  </section>

  <section class="services">
    <h2>SERVICES</h2>
    <ul>
      <li>WORKSITE RISK ASSESSMENT</li>
      <li>TRAVEL SECURITY ASSESSMENTS</li>
      <li>SPECIAL EVENT SECURITY REVIEW AND ASSESSMENT</li>
      <li>SCHOOL SAFETY AND SECURITY ASSESSMENT</li>
      <li>PERSONAL PROTECTION</li>
    </ul>
  </section>

  <svg class="hex" style="left:203px;top:650px" width="180" height="206" viewBox="0 0 180 206" role="img" aria-label="Photo of a security guard checking a driver at a car window">
    <polygon points="90,3 177,53 177,153 90,203 3,153 3,53" fill="#7c8794" stroke="#e6e8ee" stroke-width="6"/>
  </svg>
  <svg class="hex" style="left:66px;top:806px" width="226" height="254" viewBox="0 0 226 254" role="img" aria-label="Photo of a security officer monitoring camera feeds at a computer desk">
    <polygon points="113,3 223,66 223,188 113,251 3,188 3,66" fill="#c9ccd2" stroke="#e6e8ee" stroke-width="6"/>
  </svg>

  <section class="facts">
    <h2>DID YOU KNOW?</h2>
    <ul>
      <li>In 2017, there were 18,400 Victims of Workplace-Related Violence and 458 Employee Fatalities as a result. – National Workplace Safety Board, 2017</li>
      <li>$121 Billion is the annual reported corporate loss due to workplace violence. – Dana Avren, Intercross Global, 2017</li>
      <li>1,500 violent church attacks in the United States since 1999 and reported violent acts within churches are up 2,380%. – Nation Daily, 2016</li>
      <li>There has been a 452.94% increase in school gun violence and a 511.11% increase in student/faculty deaths associated with gun violence in schools over the last 5 year period (2013-2018). – Coastal Defense Graduate Institute, 2018</li>
    </ul>
  </section>

  <footer class="contact-bar">
    <div class="call">
      <span class="call-icon">
        <svg width="18" height="18" viewBox="0 0 24 24" aria-hidden="true"><path fill="#fff" d="M6.6 10.8a15.1 15.1 0 0 0 6.6 6.6l2.2-2.2a1 1 0 0 1 1-.25 11.4 11.4 0 0 0 3.6.57 1 1 0 0 1 1 1V20a1 1 0 0 1-1 1A17 17 0 0 1 3 4a1 1 0 0 1 1-1h3.5a1 1 0 0 1 1 1c0 1.25.2 2.45.57 3.6a1 1 0 0 1-.25 1z"/></svg>
      </span>
      CALL US: <strong>248-555-0147</strong>
    </div>
    <div class="web">E-MAIL: INFO@KHALVERNSECURITY.COM<br>WWW.KHALVERNSECURITY.COM</div>
  </footer>

  <nav class="social" aria-label="Social accounts">
    <span><i></i>Pagemoot · HALVERNSECURITY</span>
    <span><i></i>Snapvane · HALVERNSECURITY</span>
    <span><i></i>CareerWeft · @HALVERNSECURITY</span>
  </nav>
</main>
</body>
</html>
```